Business Card for Professional Photographer

I'm looking for an eye catching modern clean design that compliments my logo/ website fonts & colours.
I specialise in architecture, corporate & commercial photography so I'm marketing to professional clients rather than portrait / wedding clients.

I would prefer to not have a solid black design.

My logo brand guide is as follows :

Main front font. : Reislust
Main font colour : #fff
Slogan front font : Ubuntu Bold
Monogram front font : Venti Medium
Container colour : #fff

I need print ready files in pdf .png & .eps formats.

Included in the files below are some screen grabs as reference to font & colours etc.

```html
<!DOCTYPE html>
<html lang="en">
<head>
<meta charset="utf-8">
<title>Lumen Frame – Business Card</title>
<link rel="stylesheet" href="https://fonts.googleapis.com/css2?family=Open+Sans:wght@400;700&family=Ubuntu:wght@300;700&display=swap">
<style>
  :root {
    --backdrop: #3b312c;
    --card: #2c2c2d;
    --card-back: #2a2a2b;
    --pattern-light: #3a3a3c;
    --pattern-dark: #232324;
    --gold: #d7a53a;
    --white: #f4f4f4;
  }
  * { margin: 0; padding: 0; box-sizing: border-box; }
  html, body { width: 1200px; height: 847px; overflow: hidden; }
  body {
    background: var(--backdrop);
    font-family: "Open Sans", sans-serif;
    position: relative;
  }
  .card {
    position: absolute;
    width: 520px;
    height: 300px;
    border-radius: 4px;
    box-shadow: 0 14px 30px rgba(0,0,0,.45);
    overflow: hidden;
  }

  /* Back side */
  .card-back {
    left: 70px; top: 110px;
    background: var(--card-back);
  }
  .card-back .pattern {
    position: absolute; inset: 0;
    background:
      radial-gradient(circle at 30% 30%, var(--pattern-light) 0%, transparent 60%),
      linear-gradient(135deg, var(--pattern-light), var(--pattern-dark));
  }
  .card-back .back-brand {
    position: absolute;
    left: 290px; top: 196px;
    display: flex; align-items: center; gap: 10px;
  }
  .back-brand .brand-square {
    width: 34px; height: 34px;
    border: 2px solid var(--gold);
    border-radius: 3px;
  }
  .back-brand .back-name {
    font-family: "Ubuntu", sans-serif;
    font-weight: 300;
    font-size: 13px;
    letter-spacing: 3px;
    color: var(--gold);
  }

  /* Front side */
  .card-front {
    left: 610px; top: 420px;
    background: var(--card);
    color: var(--white);
  }
  .brand {
    position: absolute;
    left: 160px; top: 36px;
    display: flex; align-items: center; gap: 14px;
  }
  .brand .brand-square {
    width: 62px; height: 62px;
    border: 3px solid var(--gold);
    border-radius: 4px;
    flex: none;
  }
  .brand-name {
    font-family: "Ubuntu", sans-serif;
    font-weight: 300;
    font-size: 25px;
    letter-spacing: 5px;
    color: var(--white);
    white-space: nowrap;
  }
  .brand-slogan {
    font-family: "Ubuntu", sans-serif;
    font-weight: 700;
    font-size: 7.5px;
    letter-spacing: 2.4px;
    color: var(--gold);
    margin-top: 4px;
    white-space: nowrap;
  }
  .person {
    position: absolute;
    left: 0; right: 0; top: 120px;
    text-align: center;
  }
  .person-name {
    font-weight: 700;
    font-size: 22px;
    color: var(--gold);
    letter-spacing: .5px;
  }
  .person-role { font-size: 14px; color: var(--white); }
  .divider {
    position: absolute;
    left: 28px; right: 28px; top: 184px;
    height: 1px;
    background: var(--gold);
  }
  .contacts {
    position: absolute;
    left: 28px; top: 196px;
    list-style: none;
    font-size: 15px;
    line-height: 22px;
  }
  .contacts li { display: flex; align-items: center; gap: 5px; }
  .contacts svg { width: 11px; height: 11px; fill: var(--gold); flex: none; }
  .address {
    position: absolute;
    right: 28px; bottom: 26px;
    text-align: right;
    font-size: 16px;
    line-height: 22px;
    font-style: normal;
  }
</style>
</head>
<body>

<section class="card card-back" aria-label="Card back">
  <div class="pattern" role="img" aria-label="Embossed repeating brand pattern in charcoal tones"></div>
  <div class="back-brand">
    <span class="brand-square"></span>
    <span class="back-name">LUMEN FRAME</span>
  </div>
</section>

<section class="card card-front" aria-label="Card front">
  <div class="brand">
    <span class="brand-square"></span>
    <div>
      <div class="brand-name">LUMEN FRAME</div>
      <div class="brand-slogan">ARCHITECTURE CORPORATE COMMERCIAL</div>
    </div>
  </div>

  <div class="person">
    <div class="person-name">DANIEL HARROW</div>
    <div class="person-role">Director</div>
  </div>

  <div class="divider"></div>

  <ul class="contacts">
    <li>
      <svg viewBox="0 0 24 24" aria-hidden="true"><path d="M6.6 10.8a15 15 0 0 0 6.6 6.6l2.2-2.2a1 1 0 0 1 1-.25 11.4 11.4 0 0 0 3.6.57 1 1 0 0 1 1 1V20a1 1 0 0 1-1 1A17 17 0 0 1 3 4a1 1 0 0 1 1-1h3.5a1 1 0 0 1 1 1c0 1.25.2 2.45.57 3.57a1 1 0 0 1-.25 1z"/></svg>
      555 014 2290
    </li>
    <li>
      <svg viewBox="0 0 24 24" aria-hidden="true"><path d="M2 5h20v14H2zm2 2v.5l8 5 8-5V7l-8 5z"/></svg>
      info@lumenframe.com
    </li>
    <li>
      <svg viewBox="0 0 24 24" aria-hidden="true"><circle cx="12" cy="12" r="10"/></svg>
      www.lumenframe.com
    </li>
  </ul>

  <address class="address">
    112 Linden Row<br>
    Eastbrook NY 10452
  </address>
</section>

</body>
</html>
```